Film poster for a contemporary thriller/chase film set in Italy/Capri/Croatia

This is a poster to initially publicize the feature film, Marrow's Veil. This may become the final poster for the film but at the moment it will be used just to promote it to investors through film festivals, etc. The poster must have a sense of urgency since the film is fast-paced. Examples include Pellingworth films, Lantern of Thieves, Vesk, Calder Protocol, Margin of Embers.

Target Market(s)

Film investors, film lovers, talent agents

Industry/Entity Type

Film Production

Font styles to use
Serif

Colors

Requirements
Must have
• This is a thriller film set in modern-day Italy, Capri, and Croatia. The plot involves a young woman discovering a 2,000-year-old ring in a sea cliff on Capri. The ring was Dorvan's wedding ring and historians and others have looked for it for centuries. The woman must evade criminals, antiquities collectors, and the Vatican in an attempt to return it to its rightful heir. ELEMENTS: The mediteranean Sea, Dorvan, a gold ring with a single emerald.
Nice to have
• The idea of a woman being chased across Italy. I can supply images of the actresses's faces if that helps.
Should not have
• Cannot thik of any!

```html
<!DOCTYPE html>
<html lang="en">
<head>
<meta charset="utf-8">
<title>Marrow's Veil – Poster</title>
<link rel="stylesheet" href="https://fonts.googleapis.com/css2?family=Londrina+Solid:wght@400&family=Jost:wght@400&family=Oswald:wght@500&display=swap">
<style>
  :root {
    --paper: #ffffff;
    --orange-light: #dc5a22;
    --orange-deep: #c23b0d;
    --amber: #e38a0b;
    --ink-white: #ffffff;
    --credit-ink: #3a1405;
  }
  html, body {
    margin: 0;
    padding: 0;
    width: 1200px;
    height: 1148px;
    overflow: hidden;
    background: var(--paper);
  }
  .poster {
    position: relative;
    width: 1200px;
    height: 1148px;
    background: var(--paper);
  }
  .poster__sheet {
    position: absolute;
    top: 60px;
    left: 235px;
    width: 740px;
    height: 1030px;
    border-radius: 14px;
    background: linear-gradient(100deg, var(--orange-light), var(--orange-deep));
  }
  .poster__tagline {
    position: absolute;
    top: 124px;
    left: 235px;
    width: 740px;
    margin: 0;
    text-align: center;
    font-family: "Jost", sans-serif;
    font-size: 15px;
    letter-spacing: 0.5px;
    color: var(--ink-white);
  }
  .poster__emblem {
    position: absolute;
    top: 222px;
    left: 522px;
    width: 104px;
    height: 156px;
    border-radius: 10px;
    background: linear-gradient(180deg, rgba(255,255,255,0.35), var(--amber));
  }
  .poster__rule {
    position: absolute;
    top: 384px;
    left: 235px;
    width: 505px;
    height: 2px;
    background: var(--ink-white);
  }
  .poster__title {
    position: absolute;
    top: 392px;
    left: 235px;
    width: 740px;
    margin: 0;
    font-family: "Londrina Solid", sans-serif;
    font-weight: 400;
    color: var(--ink-white);
    text-align: center;
    line-height: 0.98;
  }
  .poster__title-line {
    display: block;
    font-size: 190px;
    letter-spacing: 4px;
  }
  .poster__credits {
    position: absolute;
    top: 930px;
    left: 250px;
    width: 710px;
    margin: 0;
    font-family: "Oswald", sans-serif;
    font-weight: 500;
    font-size: 11.5px;
    line-height: 1.45;
    text-transform: uppercase;
    text-align: center;
    color: var(--credit-ink);
    letter-spacing: 0.2px;
  }
</style>
</head>
<body>
<main class="poster">
  <div class="poster__sheet"></div>

  <p class="poster__tagline">A 2,000-YEAR-OLD MYSTERY</p>

  <div class="poster__emblem" role="img" aria-label="Emblem area: gold ring with a single stone"></div>
  <div class="poster__rule"></div>

  <h1 class="poster__title">
    <span class="poster__title-line">MARROW'S</span>
    <span class="poster__title-line">VEIL</span>
  </h1>

  <p class="poster__credits">
    Halvern Pictures presents Marrow's Veil, a thriller across the Mediterranean coast starring<br>
    Lena Vargossi, Mirelle Ostrand, Teo Branic and introducing Paola Drennick as the finder<br>
    A 2,000-year-old mystery. Written and directed by Ansel Morroway. Coming soon to cinemas
  </p>
</main>
</body>
</html>
```